Bright Tutor Circle business card

Use existing logo to design a business card which contains information that is listed below. Use of logo as attached. It is important that the colour scheme matches the logo already designed. It needs to be crisp and professional. This is an on line business, a database of training providers for educational establishments. The website will provide users with full information on trainers who are available and their credibility.
Target Market(s)
Educators and training providers
Industry/Entity Type
Education
Contact Information for Business Card
See below for details
Font styles to use
Colors
Designer to choose colors to be used in the design.
Requirements
Must have
- Email address mara@brighttutorcircle.co.uk
- Twitter feed. @MaraBtc
- LinkedIn details Mara Fenwick
- Mobile phone number 07812 540913
- Mission statement: To create a learning network that ensures that schools receive first class training that is excellent value for money.
Nice to have
- N/a
Should not have
- Twee educational images

```html
<!DOCTYPE html>
<html lang="en">
<head>
<meta charset="utf-8">
<title>Bright Tutor Circle — Business Card</title>
<link rel="stylesheet" href="https://fonts.googleapis.com/css2?family=Open+Sans:wght@400;600&display=swap">
<style>
  :root {
    --page-bg: #e9eaec;
    --card-white: #f7f7f7;
    --card-black: #1b1b1c;
    --brand-blue: #2a86c9;
    --brand-blue-light: #3aa7de;
    --band-dark: #2178bd;
    --ink: #2a2a2a;
    --ink-inverse: #ffffff;
    --dot-grey: #dcdcdc;
  }
  * { box-sizing: border-box; margin: 0; padding: 0; }
  html, body { width: 1200px; height: 1000px; overflow: hidden; }
  body {
    background: var(--page-bg);
    font-family: "Open Sans", Arial, sans-serif;
    position: relative;
  }
  .card {
    position: absolute;
    left: 270px;
    width: 660px;
    height: 377px;
    border-radius: 18px;
    overflow: hidden;
    box-shadow: 0 10px 28px rgba(0,0,0,0.18);
  }
  /* Front side */
  .card-front { top: 80px; background: var(--card-white); }
  .side-band {
    position: absolute; left: 0; top: 0; bottom: 0; width: 64px;
    background: var(--band-dark);
  }
  .side-stripe {
    position: absolute; left: 64px; top: 0; bottom: 0; width: 14px;
    background: var(--brand-blue-light);
  }
  .dot-field {
    position: absolute; right: 0; top: 0; width: 330px; height: 377px;
    background: radial-gradient(ellipse at 60% 50%, #e4e4e4 0%, #efefef 55%, var(--card-white) 100%);
  }
  .brand {
    position: absolute; display: flex; align-items: center; gap: 12px;
    color: var(--brand-blue); font-weight: 600; letter-spacing: 0.5px;
  }
  .card-front .brand { left: 112px; top: 62px; font-size: 30px; }
  .brand-mark { border-radius: 50%; background: var(--brand-blue); flex: none; }
  .card-front .brand-mark { width: 26px; height: 26px; }
  .contact-list {
    position: absolute; left: 112px; bottom: 44px;
    list-style: none; color: var(--ink); font-size: 17px; line-height: 1.55;
  }
  .contact-list li { display: flex; align-items: center; gap: 10px; }
  .contact-icon { width: 14px; height: 14px; flex: none; }
  /* Back side */
  .card-back { top: 523px; background: var(--card-black); }
  .card-back .brand {
    left: 0; right: 0; top: 92px; justify-content: center; font-size: 36px;
    color: var(--brand-blue-light);
  }
  .card-back .brand-mark { width: 32px; height: 32px; background: var(--brand-blue-light); }
  .mission {
    position: absolute; left: 110px; right: 110px; top: 196px;
    text-align: center; color: var(--ink-inverse);
    font-size: 16px; line-height: 1.55;
  }
  .rule {
    display: block; height: 2px; margin: 14px auto;
    background: linear-gradient(90deg, transparent, var(--brand-blue-light), transparent);
    width: 90%;
  }
</style>
</head>
<body>
  <section class="card card-front">
    <div class="side-band"></div>
    <div class="side-stripe"></div>
    <div class="dot-field" role="img" aria-label="Decorative pattern of soft grey dots"></div>
    <div class="brand"><span class="brand-mark"></span><span class="brand-name">Bright Tutor Circle</span></div>
    <ul class="contact-list">
      <li>
        <svg class="contact-icon" viewBox="0 0 14 14"><path d="M3 1h3l1 3-2 1a7 7 0 0 0 4 4l1-2 3 1v3a1 1 0 0 1-1 1A12 12 0 0 1 2 2a1 1 0 0 1 1-1z" fill="#2a86c9"/></svg>
        07812 540913
      </li>
      <li>
        <svg class="contact-icon" viewBox="0 0 14 14"><rect x="1" y="3" width="12" height="8" rx="1" fill="#2a86c9"/><path d="M1.5 3.5 7 8l5.5-4.5" stroke="#fff" stroke-width="1.2" fill="none"/></svg>
        mara@brighttutorcircle.co.uk
      </li>
      <li>
        <svg class="contact-icon" viewBox="0 0 14 14"><circle cx="7" cy="7" r="6" fill="#2a86c9"/></svg>
        @MaraBtc
      </li>
      <li>
        <svg class="contact-icon" viewBox="0 0 14 14"><rect x="1" y="1" width="12" height="12" rx="2" fill="#2a86c9"/></svg>
        Mara Fenwick
      </li>
    </ul>
  </section>

  <section class="card card-back">
    <div class="brand"><span class="brand-mark"></span><span class="brand-name">Bright Tutor Circle</span></div>
    <div class="mission">
      <span class="rule"></span>
      <p>To create a learning network that ensures that schools receive first class training that is excellent value for money.</p>
      <span class="rule"></span>
    </div>
  </section>
</body>
</html>
```